November Online Auction

November Online Farm and Construction Machinery Auction November 4th Thru The 7th Now Accepting Farm and Construction related Items Till November 1 St

```html
<!DOCTYPE html>
<html lang="en">
<head>
<meta charset="utf-8">
<title>November Online Auction</title>
<link rel="stylesheet" href="https://fonts.googleapis.com/css2?family=Bebas+Neue&family=Poppins:wght@400;500;700&display=swap">
<style>
  :root {
    --orange: #f7901e;
    --orange-deep: #d9772a;
    --ink: #1f1f1f;
    --charcoal: #2a2a2c;
    --slate: #5a5a5a;
    --paper: #ffffff;
    --mist: #f2f2f2;
    --stage: #a3a3a3;
  }
  html, body {
    margin: 0;
    padding: 0;
    width: 1200px;
    height: 988px;
    overflow: hidden;
    background: var(--stage);
  }
  .auction-flyer {
    position: absolute;
    left: 38px;
    top: 114px;
    width: 1124px;
    height: 760px;
    display: block;
  }
  .headline { font-family: "Bebas Neue", "Oswald", sans-serif; font-size: 93px; }
  .headline--light { fill: var(--paper); }
  .headline--dark { fill: var(--ink); }
  .brand-name { font-family: "Bebas Neue", "Oswald", sans-serif; font-size: 50px; fill: var(--orange); }
  .dates { font-family: "Bebas Neue", "Oswald", sans-serif; font-size: 88px; }
  .dates--muted { fill: var(--slate); }
  .dates--strong { fill: var(--ink); }
  .cta { font-family: "Poppins", sans-serif; font-weight: 700; font-size: 44px; fill: var(--paper); }
  .phone { font-family: "Poppins", sans-serif; font-weight: 700; font-size: 74px; fill: var(--paper); }
  .website { font-family: "Poppins", sans-serif; font-weight: 400; font-size: 31px; fill: var(--paper); }
  .website__domain { fill: var(--orange); }
  .address { font-family: "Poppins", sans-serif; font-weight: 500; font-size: 26px; fill: var(--paper); }
</style>
</head>
<body>
<svg class="auction-flyer" viewBox="0 0 1605 1085" preserveAspectRatio="none" xmlns="http://www.w3.org/2000/svg">
  <defs>
    <linearGradient id="ghost-fade" x1="0" y1="0" x2="0.6" y2="1">
      <stop offset="0" stop-color="#ffffff"/>
      <stop offset="0.4" stop-color="#f6f6f6"/>
      <stop offset="1" stop-color="#e4e4e4"/>
    </linearGradient>
    <linearGradient id="yard-tones" x1="0" y1="0" x2="0" y2="1">
      <stop offset="0" stop-color="#9ea8b4"/>
      <stop offset="0.45" stop-color="#7d7460"/>
      <stop offset="1" stop-color="#5e4c3a"/>
    </linearGradient>
    <linearGradient id="field-tones" x1="0" y1="0" x2="0" y2="1">
      <stop offset="0" stop-color="#2f7fd6"/>
      <stop offset="0.35" stop-color="#8a8f9a"/>
      <stop offset="0.55" stop-color="#c44a3a"/>
      <stop offset="1" stop-color="#8d8a85"/>
    </linearGradient>
    <filter id="frame-shadow" x="-5%" y="-5%" width="110%" height="110%">
      <feDropShadow dx="0" dy="4" stdDeviation="6" flood-color="#000" flood-opacity="0.25"/>
    </filter>
  </defs>

  <!-- Left panel -->
  <rect class="panel" x="0" y="0" width="1605" height="1085" fill="var(--paper)"/>
  <rect x="0" y="0" width="760" height="1000" fill="url(#ghost-fade)" role="img" aria-label="Faint background photo of farm machinery"/>

  <!-- Orange header -->
  <polygon points="329,0 1605,0 1605,222 722,222 606,425" fill="var(--orange)"/>
  <polygon points="329,0 507,0 417,125" fill="var(--orange-deep)"/>
  <polygon points="454,230 478,230 608,426 590,458" fill="var(--charcoal)"/>

  <!-- Photo frame -->
  <polygon points="722,222 1605,222 1605,985 812,985 492,620" fill="var(--paper)" filter="url(#frame-shadow)"/>
  <polygon points="747,242 1237,242 1002,620 1297,960 827,960 517,620" fill="url(#yard-tones)" role="img" aria-label="Photo of a yellow backhoe loader in a farm yard"/>
  <polygon points="1257,242 1605,242 1605,960 1317,960 1027,620" fill="url(#field-tones)" role="img" aria-label="Photo of a red mower conditioner parked on gravel"/>

  <!-- Bottom band -->
  <polygon points="0,863 649,863 772,1000 1605,1000 1605,1085 0,1085" fill="var(--charcoal)"/>
  <polygon points="0,840 459,840 500,910 0,910" fill="var(--orange)"/>

  <!-- Brand -->
  <circle cx="205" cy="140" r="84" fill="#8a8a8a"/>
  <text class="brand-name" x="205" y="262" text-anchor="middle">HARLOW AUCTION</text>
  <text class="brand-name" x="205" y="308" text-anchor="middle">SERVICE</text>

  <!-- Headline -->
  <text class="headline headline--light" x="1545" y="110" text-anchor="end">NOVEMBER ONLINE FARM AND</text>
  <text class="headline headline--dark" x="1545" y="188" text-anchor="end">CONSTRUCTION MACHINERY AUCTION</text>

  <!-- Dates -->
  <rect x="72" y="413" width="132" height="4" fill="var(--orange-deep)"/>
  <text class="dates dates--muted" x="72" y="496">NOVEMBER</text>
  <text class="dates dates--muted" x="72" y="568">4TH MONDAY TO</text>
  <text class="dates dates--strong" x="72" y="640">7TH NOVEMBER</text>
  <text class="dates dates--strong" x="72" y="712">THURSDAY</text>
  <rect x="72" y="735" width="364" height="4" fill="var(--orange-deep)"/>

  <!-- Contact -->
  <text class="cta" x="70" y="890">Call us Today!</text>
  <text class="phone" x="66" y="990">1 555 014-2237</text>
  <text class="website" x="70" y="1037">www.<tspan class="website__domain">harlowequipment</tspan>.com</text>

  <g class="pin-icon" transform="translate(1027,1043)">
    <path d="M0,-14 C-8,-14 -12,-8 -12,-3 C-12,5 0,16 0,16 C0,16 12,5 12,-3 C12,-8 8,-14 0,-14 Z" fill="var(--orange)"/>
    <circle cx="0" cy="-3" r="4.5" fill="var(--charcoal)"/>
  </g>
  <text class="address" x="1050" y="1053" textLength="510" lengthAdjust="spacingAndGlyphs">2480 Meadow Creek Rd. Fairview, MI 48000</text>
</svg>
</body>
</html>
```